Dietetic office: Bright Plate

I want to give my business card a modern and warm look (which attracts the eye and has a reassuring side), which links dietetics to a moment of well-being. The front and back sides must be used (not just to put the logo on the front side)

The map should be eye-catching and easy to read. I don't necessarily want to have a plain background, which I find visually weighs down the maps.
I really like the square format of a business card with rounded edges which is different from what we are used to finding (and why not take this square diagonally?), however I am not closed to another format as long as I like the style.

Who am I? Mireille, 32 years old, Dietician and passionate about food since always. I am specialized in slimming and an expert in micro nutrition, which means that I take into account not only the nutritional balance while maintaining pleasure (if foods are present in the business card, I do not want some cliché things where there would just be fruits and vegetables, but really something more global), but also the psycho-emotional dimension that I will treat with food supplements based on plants, fruits or vegetables.

-----------------------------------------------------------------------------------

 Mention to appear on the card IN FRENCH (please be careful in case of translation that the use of words is correct):

Mireille DORAN
Dietician Nutritionist
Expert in Slimming and Micro-Nutrition

Slogan: I help you lose weight sustainably with pleasure and by reconciling your events

Catchphrases: Want to lose weight? Do you like going out? Do you have a lot of events? And is pleasure on your plate important to you?

Make an appointment on Rendiplan or on 06 41 58 30 92
mireille.brightplate@exemplo-mail.fr
Address: Espace Santé, Rue des Glycines, 13990 Valmerle
www.brightplate-exemple.fr
Friendwall + Picturo Logo

- The company logo has been uploaded for your viewing. Other file formats can be made available if required.
- I would like a place for a photo of me to be possible.

Good morning,
I want to have a business card that is both lively and warm. Which will easily catch the eye while being easy to read and make people understand that I am in the field of well-being.
I like the square side in business cards (and why not use them diagonally?), or a more classic but original one.
Both the front and back sides must be used (I don't want to have the logo on just one side)
I don't want to have a plain background, but rather something more muted (I really like the suggestion from "Reed Cloud Graphic Designer" for this)
the use of logo for telephone, mail, address, rendiplan, friendwall, pictu etc is possible in order to facilitate reading

Please follow the various elements of the brief regarding the text and use the French text as it is.

I like business cards preferably square (with the possibility of using them diagonally).
The map should be eye-catching and easy to read.
It must bring pep while having softness which brings back to the well-being side
The card must be used on the front and back for the different elements (I do not want to have only the logo on the front side)
The text must correspond to the brief (be careful with the translation which can sometimes be bad)
I don't want to have a plain blue or orange background. I really like the idea of the background from "Reed Cloud Graphic Designer"

You can if you wish use symbols for contacts, telephone, rendiplan, address, fw, pictu....

Target Market(s)

mainly women between 25 and 65 years old + men around 40 years old

Contact Information for Business Card

Font styles to use
Sans Serif
Script

Colors
0054AA
0677BA
7BADD7
CADEEF
E8F1F8
0094D4
00A9DD
6FCCEA
C7EBF8
E9F6FB
00AB8E
00BBA5
67D7C9
C6EFE9
E9F9F6
FFC000
F8CF3A
FAE287
FDF2CF
FEFAEE
F0912C
F2A743
F7CA91
FBE8D2
FDF5EE

Requirements
Must have
• some pep! while being refined
Nice to have
• I really like the square format of a business card with rounded edges which is different from what we are used to finding, however I am not closed to another format as long as I like the style.
Should not have
• if foods are represented, only show fruits and vegetables (too cliché)

```html
<!DOCTYPE html>
<html lang="fr">
<head>
<meta charset="utf-8">
<title>Bright Plate – cartes de visite</title>
<link href="https://fonts.googleapis.com/css2?family=Roboto+Slab:wght@300;400&family=Cormorant+Garamond:ital,wght@1,400&display=swap" rel="stylesheet">
<style>
  :root{
    --page:#ececf2;
    --coral:#ee6e45;
    --coral-soft:#f08a66;
    --coral-deco:#f2916c;
    --tab-orange:#f7931e;
    --tab-lime:#d0dd3b;
    --tab-cyan:#2bc0d6;
    --sage:#a8c6a6;
    --card-blue:#4a92cf;
    --brand-blue:#1f6db5;
    --plate:#faf8fb;
    --white:#ffffff;
  }
  *{margin:0;padding:0;box-sizing:border-box}
  html,body{width:1200px;height:900px;overflow:hidden}
  body{background:var(--page);position:relative;font-family:"Roboto Slab",serif;font-weight:300;color:var(--white)}
  .card{position:absolute;top:208px;width:485px;height:485px;overflow:hidden}
  .card--front{left:95px;background:var(--coral)}
  .card--back{left:620px;background:var(--card-blue)}

  /* front */
  .plate{position:absolute;left:237px;top:-81px;width:244px;height:244px;border-radius:50%;background:var(--plate)}
  .brand-name{position:absolute;left:256px;top:52px;font-size:30px;font-weight:400;color:var(--brand-blue);white-space:nowrap}
  .cutlery-deco{position:absolute;left:385px;top:216px;width:96px;height:183px;border-radius:48px 48px 6px 6px;background:linear-gradient(180deg,var(--coral-deco),var(--coral))}
  .cutlery-deco--fork{left:330px;top:256px;width:42px;height:143px;border-radius:8px 8px 20px 20px}
  .tab{position:absolute;left:10px;display:flex;align-items:center;padding-left:16px;font-size:21px;line-height:1.25;border-radius:8px 0 0 8px;white-space:nowrap}
  .tab--weight{top:76px;width:227px;height:61px;background:var(--tab-orange);clip-path:polygon(0 0,91% 0,100% 100%,0 100%)}
  .tab--outings{top:146px;width:231px;height:61px;background:var(--tab-lime)}
  .tab--events{top:215px;width:416px;height:60px;background:var(--tab-cyan)}
  .tab--pleasure{top:285px;width:365px;height:61px;background:var(--sage)}
  .booking-lead{position:absolute;left:13px;top:365px;font-size:19px}
  .booking-band{position:absolute;left:0;top:398px;width:485px;height:87px;background:var(--coral-soft);display:flex;align-items:center}
  .booking-app{width:156px;height:100%;background:var(--card-blue);display:flex;align-items:center;justify-content:center;font-size:24px;font-weight:400}
  .booking-or{margin-left:14px;font-size:18px}
  .booking-phone{margin-left:22px;font-size:25px;font-weight:400;white-space:nowrap}

  /* back */
  .plate-deco{position:absolute;left:364px;top:8px;width:88px;height:88px;border-radius:50%;border:7px solid var(--tab-cyan)}
  .owner-name{position:absolute;left:30px;top:30px;font-size:31px;font-weight:400;white-space:nowrap}
  .owner-title{position:absolute;left:30px;top:74px;font-size:21px;line-height:30px;white-space:nowrap}
  .slogan-leaf{position:absolute;left:10px;top:148px;width:466px;height:105px;background:var(--sage);border-radius:150px 70px 120px 0 / 105px 70px 105px 0;display:flex;align-items:center;justify-content:center;text-align:center;font-family:"Cormorant Garamond",serif;font-style:italic;font-size:22px;line-height:24px}
  .contacts{position:absolute;left:26px;top:272px;list-style:none}
  .contact{display:flex;align-items:flex-start;font-size:20px;margin-bottom:10px;white-space:nowrap}
  .contact--web{font-size:22px}
  .contact--address{font-size:22px;line-height:30px;margin-top:10px}
  .contact-icon{width:22px;flex:none;margin:6px 10px 0 0}
  .cutlery-deco-back{position:absolute;left:340px;top:330px;width:145px;height:95px;border-radius:40px 0 0 40px;background:linear-gradient(90deg,rgba(43,192,214,.6),var(--tab-cyan))}
  .socials{position:absolute;left:395px;top:442px;display:flex;gap:16px}
  .social{width:26px;height:26px;border-radius:6px;background:var(--white);opacity:.9}
</style>
</head>
<body>
  <section class="card card--front" aria-label="Recto">
    <div class="plate"></div>
    <div class="brand-name">Bright Plate</div>
    <div class="cutlery-deco" role="img" aria-label="Couteau décoratif"></div>
    <div class="cutlery-deco cutlery-deco--fork" role="img" aria-label="Fourchette décorative"></div>
    <p class="tab tab--weight">Vous voulez<br>perdre du poids ?</p>
    <p class="tab tab--outings">Aimez-vous sortir?</p>
    <p class="tab tab--events">Avez-vous beaucoup d'événements?</p>
    <p class="tab tab--pleasure">Et le plaisir dans votre assiette<br>est-il important pour vous ?</p>
    <p class="booking-lead">Prendre rendez-vous sur</p>
    <div class="booking-band">
      <span class="booking-app">Rendiplan</span>
      <span class="booking-or">ou au</span>
      <span class="booking-phone">06 41 58 30 92</span>
    </div>
  </section>

  <section class="card card--back" aria-label="Verso">
    <div class="plate-deco" role="img" aria-label="Assiette décorative"></div>
    <h1 class="owner-name">Mireille DORAN</h1>
    <p class="owner-title">Diététicienne Nutritionniste<br>Expert en Minceur et Micro-Nutrition</p>
    <p class="slogan-leaf">Je vous aide à perdre du poids<br>durablement avec plaisir et<br>en conciliant vos événements</p>
    <div class="cutlery-deco-back" role="img" aria-label="Couteau et fourchette décoratifs"></div>
    <ul class="contacts">
      <li class="contact">
        <svg class="contact-icon" viewBox="0 0 22 16" height="14"><rect x="1" y="1" width="20" height="14" fill="none" stroke="#fff" stroke-width="1.6"/><path d="M1 1 L11 9 L21 1" fill="none" stroke="#fff" stroke-width="1.6"/></svg>
        mireille.brightplate@exemplo-mail.fr
      </li>
      <li class="contact contact--web">
        <svg class="contact-icon" viewBox="0 0 20 20" height="18"><circle cx="10" cy="10" r="8.5" fill="none" stroke="#fff" stroke-width="1.5"/><ellipse cx="10" cy="10" rx="4" ry="8.5" fill="none" stroke="#fff" stroke-width="1.5"/><path d="M1.5 10H18.5" stroke="#fff" stroke-width="1.5"/></svg>
        www.brightplate-exemple.fr
      </li>
      <li class="contact contact--address">
        <svg class="contact-icon" viewBox="0 0 16 22" height="24"><path d="M8 0C3.6 0 0 3.5 0 7.8 0 13.6 8 22 8 22s8-8.4 8-14.2C16 3.5 12.4 0 8 0z" fill="#fff"/><circle cx="8" cy="8" r="3" fill="#4a92cf"/></svg>
        <span>Espace Santé,<br>Rue des Glycines,<br>13990 Valmerle</span>
      </li>
    </ul>
    <div class="socials">
      <span class="social" role="img" aria-label="Picturo"></span>
      <span class="social" role="img" aria-label="Friendwall"></span>
    </div>
  </section>
</body>
</html>
```